Lindenkrügelhof airline passengers needs web site design

We need a website design (and a logo) for a new charity based in Switzerland. We are helping airline passengers to receive the compensation they are entiteld to by european law from the airlines in cases of delays or denied boarding or cancelled flights. Airlines often try to not pay those compensations so the passengers need assistance in receiving the compensations.

Target Market(s)

Switzerland

Industry/Entity Type

Charity

Logo Text

lindenkrügelhof.ch

Number of Pages Required

1 page

Colors

Designer to choose colors to be used in the design.

```html
<!DOCTYPE html>
<html lang="en">
<head>
<meta charset="utf-8">
<title>Lindenkrügelhof – Airline Passengers</title>
<link href="https://fonts.googleapis.com/css2?family=Oswald:wght@400;500&family=Roboto:wght@400;500;700&display=swap" rel="stylesheet">
<style>
:root{
  --orange:#e0561c;
  --orange-dark:#c9481a;
  --nav-blue:#5aaad1;
  --brand-blue:#2f9fd3;
  --cyan:#19b8e8;
  --ink:#333a40;
  --text:#4a4f54;
  --muted:#8a9096;
  --rule:#dcdfe2;
  --card-blue:#7fbedb;
  --date-blue:#7fbedb;
  --paper:#ece8e3;
  --footer:#262f36;
  --footer-text:#c9cfd4;
  --white:#ffffff;
}
*{box-sizing:border-box;margin:0;padding:0}
html,body{width:1200px;height:2675px;overflow:hidden}
body{font-family:"Roboto",Arial,sans-serif;color:var(--text);background:var(--white);position:relative}
.abs{position:absolute}
.heading{font-family:"Oswald",Arial,sans-serif;font-weight:400;text-transform:uppercase;letter-spacing:1px;color:var(--ink)}

/* header */
.site-header{position:absolute;left:0;top:0;width:1200px;height:96px;background:linear-gradient(180deg,#dfeef7 0%,#f7fbfd 60%,#ffffff 100%)}
.brand-group{position:absolute;left:73px;top:22px;height:54px;display:flex;align-items:center}
.brand{display:flex;align-items:center;gap:8px}
.brand-dot{width:18px;height:18px;border-radius:50%;background:var(--orange);flex:none}
.brand-name{font-family:"Oswald",Arial,sans-serif;font-size:19px;font-weight:500;color:var(--brand-blue);text-transform:uppercase;letter-spacing:.5px;white-space:nowrap}
.brand-divider{width:1px;height:50px;background:var(--rule);margin:0 14px 0 14px;flex:none}
.brand-tagline{font-size:22px;color:var(--ink);white-space:nowrap}
.social{position:absolute;top:30px;display:flex;gap:8px}
.social-box{width:38px;height:38px;background:#3a4248}
.donate-top{position:absolute;left:1006px;top:30px;width:118px;height:40px;background:var(--orange);border-radius:3px;color:var(--white);font-family:"Oswald",Arial,sans-serif;font-size:17px;display:flex;align-items:center;justify-content:center;text-transform:uppercase}
.main-nav{position:absolute;left:0;top:96px;width:1200px;height:47px;background:var(--nav-blue);border-top:3px solid #8cc6e2}
.main-nav ul{list-style:none;display:flex;gap:34px;padding-left:91px;height:100%;align-items:center}
.main-nav a{color:var(--white);text-decoration:none;font-family:"Oswald",Arial,sans-serif;font-size:17px;text-transform:uppercase}

/* hero */
.hero{position:absolute;left:0;top:143px;width:1200px;height:588px;background:radial-gradient(ellipse at 40% 40%,#a4403f 0%,#7a6a64 22%,#5b5f63 50%,#3c4247 100%)}
.hero-text{position:absolute;left:73px;top:240px;font-family:"Oswald",Arial,sans-serif;font-weight:500;font-size:33px;line-height:40px;color:var(--white);text-transform:uppercase}
.btn-orange{background:var(--orange);color:var(--white);font-family:"Oswald",Arial,sans-serif;text-transform:uppercase;display:flex;align-items:center;justify-content:center;border-radius:3px}
.hero .btn-orange{position:absolute;left:73px;top:328px;width:120px;height:42px;font-size:17px}

/* welcome */
.welcome-title{left:73px;top:770px;font-size:28px;white-space:nowrap}
.welcome-title span{color:var(--brand-blue)}
.welcome-rule{left:73px;top:817px;width:785px;height:1px;background:var(--rule)}
.welcome-body{left:73px;top:836px;width:785px;font-size:13.5px;line-height:24px}
.welcome-body p+p{margin-top:22px}
.read-more{font-size:13px;font-weight:700;color:var(--ink);text-transform:uppercase}
.join-box{position:absolute;left:884px;top:776px;width:241px;height:330px;background:linear-gradient(135deg,var(--orange) 0%,var(--orange-dark) 100%);padding:22px 18px;color:var(--white)}
.join-box h3{font-family:"Oswald",Arial,sans-serif;font-weight:500;font-size:26px;line-height:28px}
.join-box h4{font-family:"Oswald",Arial,sans-serif;font-weight:400;font-size:22px;text-transform:uppercase;border-bottom:1px solid rgba(255,255,255,.5);padding-bottom:10px}
.join-box p{font-size:15px;line-height:27px;margin-top:14px}
.join-btn{position:absolute;left:18px;bottom:20px;width:205px;height:38px;background:var(--cyan);color:var(--white);font-size:15px;font-weight:500;display:flex;align-items:center;justify-content:center}

/* mission */
.mission{position:absolute;left:0;top:1153px;width:1200px;height:300px;background:linear-gradient(90deg,#4c5257 0%,#6b7075 50%,#484e53 100%)}
.mission-title{position:absolute;left:0;width:1200px;top:44px;display:flex;justify-content:center;align-items:center;gap:14px;color:var(--white);font-size:28px}
.mission-flag{width:36px;height:22px;fill:var(--white)}
.mission p{position:absolute;left:150px;width:900px;top:110px;text-align:center;color:#eef0f2;font-size:19px;line-height:27px}

/* news & testimonials */
.section-label{font-size:20px}
.news-item{position:absolute;left:73px;width:336px;height:70px;border-bottom:1px solid var(--rule)}
.date{position:absolute;left:0;top:0;width:52px;height:54px;background:var(--date-blue);color:var(--white);text-align:center;font-family:"Oswald",Arial,sans-serif}
.date .m{font-size:9px;display:block;padding-top:3px}
.date .d{font-size:22px;line-height:22px;display:block}
.date .y{font-size:9px;display:block}
.news-item p{position:absolute;left:63px;top:6px;font-size:13.5px;line-height:24px;color:var(--ink);font-weight:500}
.slider-arrows{position:absolute;left:1084px;top:1497px;display:flex;gap:3px}
.slider-arrows svg{width:19px;height:19px}
.quote-card{position:absolute;top:1546px;width:334px;height:340px;border:1px solid #cfd4d8;border-radius:4px;overflow:hidden;background:var(--white)}
.quote-card blockquote{padding:20px 20px 0;font-size:15.5px;line-height:24.5px;color:var(--text)}
.quote-foot{position:absolute;left:0;bottom:0;width:100%;height:109px;background:var(--card-blue);text-align:center;color:var(--white)}
.avatar{position:absolute;left:50%;top:-48px;margin-left:-44px;width:88px;height:88px;border-radius:50%;background:linear-gradient(180deg,#c7b3a4,#8c7a6e);border:4px solid var(--card-blue)}
.quote-foot strong{display:block;margin-top:50px;font-size:17px}
.quote-foot span{font-size:16px}

/* videos */
.videos{position:absolute;left:0;top:1934px;width:1200px;height:467px;background:var(--paper)}
.videos-title{position:absolute;left:0;width:1200px;top:50px;text-align:center;font-size:28px}
.video{position:absolute;top:127px;width:423px;height:232px}
.video-1{left:164px;background:linear-gradient(160deg,#5f6e7b 0%,#3c4a58 60%,#2f3b48 100%)}
.video-2{left:613px;background:linear-gradient(160deg,#3f5a6a 0%,#6b6f6c 50%,#1f8fa6 100%)}
.play{position:absolute;left:50%;top:50%;width:108px;height:108px;margin:-54px 0 0 -54px}
.video-caption{position:absolute;top:372px;width:423px;font-size:13.5px;line-height:24px;color:var(--text)}

/* footer */
.site-footer{position:absolute;left:0;top:2401px;width:1200px;height:274px;background:var(--footer);color:var(--footer-text)}
.foot-brand{position:absolute;left:73px;top:52px;display:flex;align-items:center;gap:7px}
.foot-brand .brand-dot{width:15px;height:15px}
.foot-brand .brand-name{font-size:16px}
.foot-tagline{position:absolute;left:73px;top:118px;width:186px;text-align:center;font-size:21px;line-height:26px;color:#a9b1b8}
.foot-h{position:absolute;top:46px;font-size:12px;font-weight:700;color:var(--nav-blue);text-transform:uppercase;letter-spacing:.5px}
.foot-p{position:absolute;font-size:12.5px;line-height:26px;color:var(--white)}
.email-field{position:absolute;left:505px;top:143px;width:208px;height:32px;background:var(--white);display:flex;align-items:center;justify-content:space-between;padding:0 8px 0 10px;font-size:13px;color:#555}
.foot-links{list-style:none;position:absolute;top:80px;font-size:13px;line-height:26px;color:var(--white)}
.foot-social{position:absolute;left:995px;top:85px;display:flex;gap:10px}
.foot-social span{width:18px;height:18px;background:#9aa3aa}
.foot-rule{position:absolute;left:73px;top:220px;width:1052px;height:1px;background:#3a444c}
.foot-small{position:absolute;top:244px;font-size:12px;color:var(--nav-blue);text-transform:uppercase}
</style>
</head>
<body>

<header class="site-header">
  <div class="brand-group">
    <div class="brand"><span class="brand-dot"></span><span class="brand-name">Lindenkrügelhof</span></div>
    <span class="brand-divider"></span>
    <span class="brand-tagline">Airline Passengers</span>
  </div>
  <div class="social" style="left:910px"><span class="social-box" aria-label="Social profile"></span><span class="social-box" aria-label="Social profile"></span></div>
  <a class="donate-top">Donate Now</a>
</header>

<nav class="main-nav">
  <ul>
    <li><a>Home</a></li><li><a>About Us</a></li><li><a>Passengers</a></li><li><a>Volunteers</a></li>
    <li><a>Events</a></li><li><a>Participation</a></li><li><a>News</a></li><li><a>Contact Us</a></li>
  </ul>
</nav>

<section class="hero" role="img" aria-label="Hands holding a red fabric heart, with a traveller looking out of an aircraft window">
  <h1 class="hero-text">Lorem ipsum dolor sit amet,<br>consectetur adipiscing elit,</h1>
  <a class="btn-orange">Donate Now</a>
</section>

<section>
  <h2 class="abs heading welcome-title">Welcome to <span>Lindenkrügelhof Airline Passengers</span></h2>
  <div class="abs welcome-rule"></div>
  <div class="abs welcome-body">
    <p>Lorem Ipsum is simply dummy text of the printing and typesetting industry. Lorem Ipsum has been the industry's standard dummy text ever since the 1500s, when an unknown printer took a galley of type and scrambled it to make a type specimen book. It has survived not only five centuries, but also the leap into electronic typesetting, remaining essentially unchanged. It was popularised in the 1960s with the release of Letraset sheets containing Lorem Ipsum passages, and more recently with desktop publishing software like Aldus PageMaker including versions of Lorem Ipsum.</p>
    <p>Lorem ipsum dolor sit amet, consectetur adipiscing elit, sed do eiusmod tempor incididunt ut labore et dolore magna aliqua. Ut enim ad minim veniam, quis nostrud exercitation ullamco laboris nisi ut aliquip ex ea commodo consequat. Duis aute irure dolor in reprehenderit in voluptate velit esse cillum dolore eu fugiat nulla pariatur. Excepteur sint occaecat cupidatat non proident, sunt in culpa qui officia deserunt mollit anim id est laborum.</p>
    <p class="read-more" style="margin-top:18px">Read More &#9656;</p>
  </div>
  <aside class="join-box">
    <h3>JOIN</h3>
    <h4>Lindenkrügelhof</h4>
    <p>Lorem ipsum dolor sit amet, consectetur adipiscing elit, sed do eiusmod tempor incididunt ut labore et dolore magna aliqua.</p>
    <a class="join-btn">Join Now</a>
  </aside>
</section>

<section class="mission">
  <h2 class="mission-title heading" style="color:var(--white)">
    <svg class="mission-flag" viewBox="0 0 36 22"><polygon points="0,0 36,0 30,22 6,22"/></svg>
    Our Mission
    <svg class="mission-flag" viewBox="0 0 36 22"><polygon points="6,0 36,0 30,22 0,22"/></svg>
  </h2>
  <p>Lorem ipsum dolor sit amet, consectetur adipiscing elit, sed do eiusmod tempor incididunt ut labore et dolore magna aliqua. Ut enim ad minim veniam, quis nostrud exercitation ullamco laboris nisi ut aliquip ex ea commodo consequat. Lorem ipsum dolor sit amet, consectetur adipiscing elit, sed do eiusmod tempor incididunt ut labore et dolore magna aliqua. Ut enim ad minim veniam, quis nostrud exercitation ullamco laboris nisi ut aliquip ex ea commodo consequat.</p>
</section>

<section>
  <h3 class="abs heading section-label" style="left:73px;top:1493px">Latest News</h3>
  <article class="news-item" style="top:1546px"><div class="date"><span class="m">JUL</span><span class="d">25</span><span class="y">2017</span></div><p>Lorem ipsum dolor sit amet, consectetur adipiscing elit,</p></article>
  <article class="news-item" style="top:1629px"><div class="date"><span class="m">JUL</span><span class="d">23</span><span class="y">2017</span></div><p>Lorem ipsum dolor sit amet, consectetur adipiscing elit,</p></article>
  <article class="news-item" style="top:1712px"><div class="date"><span class="m">JUL</span><span class="d">20</span><span class="y">2017</span></div><p>Lorem ipsum dolor sit amet, consectetur adipiscing elit,</p></article>
  <article class="news-item" style="top:1795px"><div class="date"><span class="m">JUL</span><span class="d">18</span><span class="y">2017</span></div><p>Lorem ipsum dolor sit amet, consectetur adipiscing elit,</p></article>
  <p class="abs read-more" style="left:73px;top:1874px">Read More &#9656;</p>

  <h3 class="abs heading section-label" style="left:433px;top:1493px">What people are saying about us</h3>
  <div class="slider-arrows">
    <svg viewBox="0 0 20 20"><circle cx="10" cy="10" r="8.5" fill="none" stroke="#6b7278" stroke-width="1.4"/><polyline points="11.5,6 7.5,10 11.5,14" fill="none" stroke="#6b7278" stroke-width="1.6"/></svg>
    <svg viewBox="0 0 20 20"><circle cx="10" cy="10" r="8.5" fill="none" stroke="#333a40" stroke-width="1.4"/><polyline points="8.5,6 12.5,10 8.5,14" fill="none" stroke="#333a40" stroke-width="1.6"/></svg>
  </div>
  <figure class="quote-card" style="left:433px">
    <blockquote>"Lorem ipsum dolor sit amet, consectetur adipiscing elit, sed do eiusmod tempor incididunt ut labore et dolore magna aliqua. Ut enim ad minim veniam, quis nostrud aliquip ex ea commodo consequat."</blockquote>
    <figcaption class="quote-foot"><div class="avatar" role="img" aria-label="Portrait photo of Lukas Brunner"></div><strong>Lukas Brunner</strong><span>Lorem ipsum dolor</span></figcaption>
  </figure>
  <figure class="quote-card" style="left:792px">
    <blockquote>"Lorem ipsum dolor sit amet, consectetur adipiscing elit, sed do eiusmod tempor incididunt ut labore et dolore magna aliqua. Ut enim ad minim veniam, quis nostrud aliquip ex ea commodo consequat."</blockquote>
    <figcaption class="quote-foot"><div class="avatar" role="img" aria-label="Portrait photo of Marco Keller"></div><strong>Marco Keller</strong><span>Lorem ipsum dolor</span></figcaption>
  </figure>
</section>

<section class="videos">
  <h2 class="videos-title heading">Watch Lindenkrügelhof in action</h2>
  <div class="video video-1" role="img" aria-label="Video still of a group of volunteers standing together">
    <svg class="play" viewBox="0 0 108 108"><circle cx="54" cy="54" r="51" fill="rgba(0,0,0,.15)" stroke="#fff" stroke-width="3"/><polygon points="44,34 76,54 44,74" fill="#fff"/></svg>
  </div>
  <div class="video video-2" role="img" aria-label="Video still of volunteers talking with a clipboard">
    <svg class="play" viewBox="0 0 108 108"><circle cx="54" cy="54" r="51" fill="rgba(0,0,0,.15)" stroke="#fff" stroke-width="3"/><polygon points="44,34 76,54 44,74" fill="#fff"/></svg>
  </div>
  <p class="video-caption" style="left:164px">Lorem ipsum dolor sit amet, consectetur adipiscing elit, sed do eiusmod tempor incididunt ut labore et dolore magna aliqua.</p>
  <p class="video-caption" style="left:613px">Lorem ipsum dolor sit amet, consectetur adipiscing elit, sed do eiusmod tempor incididunt ut labore et dolore magna aliqua.</p>
</section>

<footer class="site-footer">
  <div class="foot-brand"><span class="brand-dot"></span><span class="brand-name">Lindenkrügelhof</span></div>
  <div class="foot-tagline">Airline<br>Passengers</div>

  <h4 class="foot-h" style="left:275px">Contact Us</h4>
  <p class="foot-p" style="left:275px;top:80px">857 Lorem ipsum dolor<br>Sit Amet, Suite 2A</p>
  <p class="foot-p" style="left:275px;top:142px">Phone: 100 000 000<br>Email: info@lindenkruegelhof.ch</p>

  <h4 class="foot-h" style="left:505px">Subscribe to our newsletter</h4>
  <p class="foot-p" style="left:505px;top:80px;width:230px;font-weight:500">Lorem ipsum dolor sit amet, conse ctetur adipiscing elit,</p>
  <div class="email-field"><span>Enter your email</span>
    <svg width="26" height="18" viewBox="0 0 26 18"><rect x="1" y="1" width="24" height="16" fill="none" stroke="#555" stroke-width="1.4"/><polyline points="1,1 13,10 25,1" fill="none" stroke="#555" stroke-width="1.4"/></svg>
  </div>

  <h4 class="foot-h" style="left:797px">Quick Links</h4>
  <ul class="foot-links" style="left:797px"><li>Home</li><li>About Us</li><li>Passengers</li><li>Volunteers</li></ul>
  <ul class="foot-links" style="left:900px"><li>Events</li><li>Participation</li><li>News</li><li>Contact Us</li></ul>

  <h4 class="foot-h" style="left:995px">Connect with us</h4>
  <div class="foot-social"><span aria-label="Social profile"></span><span aria-label="Social profile"></span></div>

  <div class="foot-rule"></div>
  <p class="foot-small" style="left:73px">© 2017 Lindenkrügelhof</p>
  <p class="foot-small" style="right:75px">Privacy &amp; Cookies Policy</p>
</footer>

</body>
</html>
```